Travel video blogger needs website design

I need a website designed for my new travel video blog "Roaming Sparrow". I have only just started but need a website that is fairly simple and not too busy. I have a logo which I want on it (I have attached it to this project). I also want a link to all my other social medias on the main page (vidtrekhub, Snapwell and Palnook) and my videos as well. Here is a link to my vidtrekhub page for you to look at: https://www.vidtrekhub.net/channel/QRm4tZ8pWnE2HX57YKccd31v
As I have only just started and I am still trying to find my specific niche, again I need it to be sleek and simple that I can go in and change slightly here and there. I would like these pages on the website: About Me, Videos, Social Media, Blog, Gallery, contact me. for an example I like the look of www.theroamingkinfolk.net website.

I already have the domain and I am with Harborweb with pagecraftr.org. I just want to spend my time getting better and learning about videos then trying to create a website (I am a bit of a perfectionist when I try to do something).

Target Market(s)

Young Adults (majority females) between the ages of 18 and 30 with an interest in travelling.

Industry/Entity Type

Travel Industry

Number of Pages Required

1 page

Colors

Designer to choose colors to be used in the design.

Requirements
Must have
• A like to my Snapwell, Palnook and vidtrekhub channels on the home page
• Must be a nice, simple design
• Must have my logo on the front and name "Roaming Sparrow"
Nice to have
• A nice light, bright coloured theme
Should not have
• A dark coloured theme

```html
<!DOCTYPE html>
<html lang="en">
<head>
<meta charset="utf-8">
<title>Roaming Sparrow — Travel Video Blog</title>
<link rel="stylesheet" href="https://fonts.googleapis.com/css2?family=Noto+Serif:wght@400&family=Raleway:wght@400;600&display=swap">
<style>
:root{
  --page:#faf6f0;
  --panel:#ffffff;
  --panel-dark:#ece3d6;
  --gold:#b8772e;
  --gold-soft:#d2a878;
  --text:#3b332b;
  --muted:#6f665c;
  --nav:#3b2d1f;
  --line:#e6dac9;
  --outside:#ffffff;
}
*{margin:0;padding:0;box-sizing:border-box}
html,body{width:1200px;height:1200px;overflow:hidden;background:var(--outside)}
.stage{position:absolute;left:0;top:0;width:1500px;height:1500px;transform:scale(.8);transform-origin:0 0}
.page{position:absolute;left:477px;top:0;width:545px;height:1500px;background:var(--page);overflow:hidden}
.abs{position:absolute}
.serif{font-family:"Noto Serif",Georgia,serif}
.sans{font-family:"Raleway",Arial,sans-serif}
.hero-photo{left:0;top:0;width:545px;height:270px;background:linear-gradient(180deg,#f1dcc0 0%,#f3e3cd 35%,#f7ede1 70%,var(--page) 100%)}
.guides{left:0;top:0}
.logo{left:84px;top:5px;width:96px;text-align:center}
.logo-mark{width:30px;height:30px;border:1.5px solid var(--gold);border-radius:50%;margin:0 auto 6px}
.logo-name{font-size:7.5px;color:var(--gold);letter-spacing:.4px;white-space:nowrap}
.nav{left:220px;top:27px;display:flex;gap:11px;font-size:8.5px;color:var(--nav)}
.nav .active{color:var(--gold)}
.panel{background:var(--panel);box-shadow:0 2px 10px rgba(120,90,50,.08)}
.shadow{background:var(--panel-dark)}
.h2{font-size:16px;color:var(--gold);line-height:1;font-weight:400}
.rule{height:1px;width:25px;background:var(--gold)}
.welcome-copy{font-size:8.3px;line-height:9.8px;color:var(--text);width:90px}
.social-links{font-size:6.4px;color:var(--gold);display:flex;gap:5px;white-space:nowrap}
.play{left:91px;top:71px}
.body-small{font-size:4.4px;line-height:7.6px;color:var(--muted)}
.btn{border:1px solid var(--gold-soft);color:var(--gold);font-size:3.8px;font-weight:600;letter-spacing:.3px;display:flex;align-items:center;justify-content:center;white-space:nowrap}
.card-title{font-size:5.5px;color:var(--gold)}
.card-rule{height:1px;background:var(--gold-soft)}
.read-more{font-size:3.8px;font-weight:600;color:var(--gold);letter-spacing:.3px}
.field{border-bottom:1px solid #d8cdbf;font-size:3.8px;color:var(--muted);padding-bottom:4px}
.social-box{width:40px;height:22px;border:1px solid var(--gold-soft);color:var(--gold);font-size:5px;display:flex;align-items:center;justify-content:center}
.copyright{font-size:7px;color:var(--gold);white-space:nowrap}
</style>
</head>
<body>
<div class="stage">
<main class="page">
  <div class="abs hero-photo" role="img" aria-label="Soft sunrise over hills and forest"></div>

  <svg class="abs guides" width="545" height="1500" aria-hidden="true">
    <g stroke="#eadfcf" stroke-width="1" fill="none">
      <line x1="0" y1="260" x2="545" y2="470"/>
      <line x1="545" y1="480" x2="220" y2="720"/>
      <line x1="0" y1="915" x2="545" y2="1140"/>
      <line x1="0" y1="920" x2="170" y2="790"/>
      <line x1="0" y1="1490" x2="300" y2="1310"/>
    </g>
  </svg>

  <header>
    <div class="abs logo sans">
      <div class="logo-mark"></div>
      <div class="logo-name">ROAMING SPARROW</div>
    </div>
    <nav class="abs nav serif">
      <span class="active">Home</span><span>About me</span><span>Videos</span><span>Blog</span><span>Gallery</span><span>Contact me</span>
    </nav>
  </header>

  <section class="welcome">
    <div class="abs shadow" style="left:440px;top:80px;width:9px;height:153px"></div>
    <div class="abs panel" style="left:94px;top:80px;width:130px;height:153px"></div>
    <h1 class="abs h2 serif" style="left:111px;top:94px">Welcome</h1>
    <div class="abs rule" style="left:111px;top:114px"></div>
    <p class="abs welcome-copy serif" style="left:112px;top:128px">Roaming Sparrow is a personal travel video blog. Here i will be posting videos and articles of all my adventures around the world.</p>
    <div class="abs social-links serif" style="left:111px;top:222px"><span>Palnook</span><span>vidtrekhub</span><span>Snapwell</span></div>
    <div class="abs" style="left:223px;top:68px;width:217px;height:178px;background:linear-gradient(135deg,#f1e2cc 0%,#e2b98f 40%,#d08f6f 70%,#b8a596 100%)" role="img" aria-label="Traveller reading a map beside railway tracks at sunset">
      <svg class="abs play" width="36" height="36" aria-hidden="true"><circle cx="18" cy="18" r="16" fill="none" stroke="#fff" stroke-width="2.5"/><path d="M14 11 L25 18 L14 25 Z" fill="#fff"/></svg>
    </div>
  </section>

  <section class="about">
    <div class="abs panel" style="left:94px;top:273px;width:355px;height:152px"></div>
    <h2 class="abs h2 serif" style="left:113px;top:289px">About me</h2>
    <div class="abs rule" style="left:113px;top:309px"></div>
    <p class="abs body-small sans" style="left:113px;top:319px;width:130px">Lorem ipsum dolor sit amet, consectetur adipiscing elit, sed do eiusmod tempor incididunt ut labore et dolore magna aliqua. Ut enim ad minim veniam, quis nostrud exercitation ullamco laboris nisi ut aliquip ex ea commodo consequat.</p>
    <p class="abs body-small sans" style="left:113px;top:357px;width:130px">Duis aute irure dolor in reprehenderit in voluptate velit esse cillum dolore eu fugiat nulla pariatur. Excepteur sint occaecat cupidatat non proident.</p>
    <div class="abs btn sans" style="left:113px;top:393px;width:50px;height:16px">READ MORE</div>
    <div class="abs" style="left:271px;top:260px;width:160px;height:178px;background:linear-gradient(180deg,#9dbde0 0%,#d3deea 40%,#97a4b3 65%,#6d7886 100%)" role="img" aria-label="Man standing by a calm lake under a blue sky"></div>
  </section>

  <section class="articles">
    <h2 class="abs h2 serif" style="left:215px;top:501px">Lastest articles</h2>
    <div class="abs rule" style="left:215px;top:520px"></div>

    <div class="abs shadow" style="left:94px;top:547px;width:93px;height:65px"></div>
    <div class="abs" style="left:102px;top:556px;width:92px;height:63px;background:linear-gradient(160deg,#a9b3c6,#9a918a 60%,#7d6d5c)" role="img" aria-label="Eagle in flight"></div>
    <div class="abs card-title serif" style="left:94px;top:629px">Lorem Ipsum Dolor</div>
    <div class="abs card-rule" style="left:94px;top:639px;width:101px"></div>
    <p class="abs body-small sans" style="left:94px;top:646px;width:101px">Lorem ipsum dolor sit amet, consectetur piscing elit, sed do eiusmod tempor incididunt ut labore et dolore magna aliqua. Ut enim ad minim veniam quis nostrud exercitation.</p>
    <div class="abs read-more sans" style="left:94px;top:685px">READ MORE &nbsp;›</div>

    <div class="abs shadow" style="left:223px;top:570px;width:92px;height:65px"></div>
    <div class="abs" style="left:230px;top:578px;width:93px;height:64px;background:linear-gradient(180deg,#e0b878 0%,#c4924f 50%,#8a6233 100%)" role="img" aria-label="Golden misty forest"></div>
    <div class="abs card-title serif" style="left:222px;top:653px">Lorem Ipsum Dolor</div>
    <div class="abs card-rule" style="left:222px;top:663px;width:101px"></div>
    <p class="abs body-small sans" style="left:222px;top:670px;width:101px">Lorem ipsum dolor sit amet, consectetur piscing elit, sed do eiusmod tempor incididunt ut labore et dolore magna aliqua. Ut enim ad minim veniam quis nostrud exercitation.</p>
    <div class="abs read-more sans" style="left:222px;top:708px">READ MORE &nbsp;›</div>

    <div class="abs shadow" style="left:350px;top:547px;width:93px;height:65px"></div>
    <div class="abs" style="left:358px;top:555px;width:93px;height:64px;background:linear-gradient(180deg,#d3d1cc 0%,#a8998a 55%,#7c6a57 100%)" role="img" aria-label="Brown bear on a rocky slope"></div>
    <div class="abs card-title serif" style="left:349px;top:629px">Lorem Ipsum Dolor</div>
    <div class="abs card-rule" style="left:349px;top:639px;width:102px"></div>
    <p class="abs body-small sans" style="left:349px;top:646px;width:101px">Lorem ipsum dolor sit amet, consectetur piscing elit, sed do eiusmod tempor incididunt ut labore et dolore magna aliqua. Ut enim ad minim veniam quis nostrud exercitation.</p>
    <div class="abs read-more sans" style="left:349px;top:685px">READ MORE &nbsp;›</div>
  </section>

  <section class="gallery">
    <h2 class="abs h2 serif" style="left:113px;top:775px">Gallery</h2>
    <div class="abs rule" style="left:113px;top:794px"></div>
    <div class="abs" style="left:113px;top:824px;width:101px;height:94px;background:linear-gradient(180deg,#e8ecec 0%,#8fa868 40%,#74954f 100%)" role="img" aria-label="Winding road through green hills"></div>
    <div class="abs" style="left:222px;top:804px;width:101px;height:94px;background:linear-gradient(180deg,#8c8272 0%,#a48f62 50%,#857540 100%)" role="img" aria-label="Foggy golden moorland"></div>
    <div class="abs" style="left:331px;top:843px;width:101px;height:55px;background:linear-gradient(120deg,#8f9d62,#c9ba82 60%,#7d7a4a)" role="img" aria-label="Sunlit forest branch"></div>
    <div class="abs" style="left:222px;top:908px;width:233px;height:95px;background:linear-gradient(180deg,#868a78 0%,#5d8a4c 45%,#3d5a40 72%,#cdd8e4 100%)" role="img" aria-label="Mountain ridge reflected in a lake"></div>
    <div class="abs" style="left:93px;top:927px;width:121px;height:152px;background:linear-gradient(180deg,#a9a599 0%,#857760 55%,#ab9f7e 100%)" role="img" aria-label="Hiker sitting with a dog on a misty cliff"></div>
    <div class="abs" style="left:222px;top:1010px;width:101px;height:96px;background:linear-gradient(135deg,#4f7246,#6f9152 50%,#4a6240)" role="img" aria-label="Aerial view of green valleys"></div>
    <div class="abs" style="left:331px;top:1010px;width:101px;height:56px;background:linear-gradient(90deg,#666a6e,#b4bac0 50%,#5c6064)" role="img" aria-label="Tall misty pine forest"></div>
    <div class="abs btn sans" style="left:247px;top:1131px;width:50px;height:16px">SHOW MORE</div>
  </section>

  <section class="contact">
    <div class="abs panel" style="left:94px;top:1213px;width:355px;height:152px"></div>
    <div class="abs" style="left:113px;top:1200px;width:160px;height:179px;background:linear-gradient(160deg,#a08a70 0%,#c9a06e 40%,#a47f56 70%,#e4dccf 100%)" role="img" aria-label="Bundle of old letters tied with string beside a pen"></div>
    <h2 class="abs h2 serif" style="left:304px;top:1229px">Contact</h2>
    <div class="abs rule" style="left:304px;top:1249px"></div>
    <div class="abs field sans" style="left:304px;top:1266px;width:59px">Your name</div>
    <div class="abs field sans" style="left:374px;top:1266px;width:58px">Your email</div>
    <div class="abs field sans" style="left:304px;top:1288px;width:128px;height:26px">Message</div>
    <div class="abs btn sans" style="left:303px;top:1333px;width:49px;height:16px">SEND MESSAGE</div>
  </section>

  <footer>
    <div class="abs social-box sans" style="left:206px;top:1431px">Palnook</div>
    <div class="abs social-box sans" style="left:251px;top:1431px">vidtrekhub</div>
    <div class="abs social-box sans" style="left:296px;top:1431px">Snapwell</div>
    <div class="abs copyright serif" style="left:285px;top:1481px">CopyRight RoamingSparrow 2018 All Rights Reserved</div>
  </footer>
</main>
</div>
</body>
</html>
```